Beacon Law Stationary - Law Firm

I am looking for a designer who can help me design letterhead and envelopes consistent with our new business cards. Feel free to reach out to me directly at ned@beaconlawgroup.example. Thank you!! Visit beaconlawgroup.example to see our site and the attached files for creative assets.

Target Market(s)

Anyone needing a lawyer

Font styles to use
Other font styles liked:
• Adobe Caslon Pro

Requirements
Must have
• Adobe Caslon Pro font
Full color
Nice to have
• My photo on front along with 2/3 face of camo - see mock up for example of what I have in mind.

American colors - similar to the ones found on my website and gold.

```html
<!DOCTYPE html>
<html lang="en">
<head>
<meta charset="utf-8">
<title>Beacon Law Stationery</title>
<link rel="stylesheet" href="https://fonts.googleapis.com/css2?family=Libre+Caslon+Text:ital,wght@0,400;1,400&family=Didact+Gothic&family=Roboto:wght@500;700&display=swap">
<style>
  :root {
    --navy: #0d1f4c;
    --navy-deep: #001a47;
    --gold: #c9a443;
    --gold-light: #f6eec4;
    --gold-bright: #f3c638;
    --ink: #1d1d1d;
    --blue-head: #1b3f8a;
    --stage-dark: #484848;
    --stage-light: #e7e7e7;
    --paper: #ffffff;
  }
  * { box-sizing: border-box; margin: 0; padding: 0; }
  html, body { width: 1200px; height: 2189px; overflow: hidden; }
  body { position: relative; background: var(--stage-light); font-family: "Didact Gothic", sans-serif; color: var(--ink); }

  .stage-dark { position: absolute; left: 0; top: 0; width: 1200px; height: 1354px; background: var(--stage-dark); }
  .stage-light { position: absolute; left: 0; top: 1354px; width: 1200px; height: 835px; background: radial-gradient(ellipse at 55% 30%, #f4f4f4, #dcdcdc); }

  /* Letterhead */
  .letterhead { position: absolute; width: 719px; height: 931px; background: var(--paper); overflow: hidden; transform-origin: 0 0; }
  .letterhead--main { left: 240px; top: 36px; }
  .letterhead--mini { left: 548px; top: 1489px; transform: scale(0.619); }

  .lh-header { position: absolute; left: 0; top: 0; width: 719px; height: 87px; background: var(--navy); }
  .lh-header svg { position: absolute; left: 0; top: 0; }
  .brand-mark { position: absolute; left: 44px; top: 26px; width: 28px; height: 28px; border-radius: 50%; border: 2px solid var(--gold); }
  .brand-name { position: absolute; left: 84px; top: 28px; font-family: "Libre Caslon Text", serif; font-size: 23px; letter-spacing: 1.5px; color: var(--gold); line-height: 1; }
  .tagline { position: absolute; right: 26px; top: 56px; font-family: "Libre Caslon Text", serif; font-style: italic; font-size: 17.5px; color: var(--navy); line-height: 1; }

  .date-line { position: absolute; left: 518px; top: 123px; font-family: "Libre Caslon Text", serif; font-size: 13px; }
  .date-line span { display: inline-block; width: 94px; border-bottom: 1px solid var(--ink); margin-left: 4px; }

  .lh-body { position: absolute; left: 54px; top: 0; width: 620px; font-size: 13.6px; line-height: 17px; white-space: nowrap; }
  .lh-body .block { position: absolute; left: 0; }
  .section-key { font-family: "Roboto", sans-serif; font-weight: 500; font-size: 15px; color: var(--blue-head); letter-spacing: 0.3px; }
  .section-title { font-family: "Roboto", sans-serif; font-weight: 500; font-size: 12.5px; color: var(--ink); left: -1px !important; }
  .check-item { position: absolute; left: 0; padding-left: 24px; }
  .check-item svg { position: absolute; left: 0; top: 2px; }

  .lh-footer { position: absolute; left: 0; top: 853px; width: 719px; height: 78px; }
  .lh-footer svg { position: absolute; left: 0; top: 0; }
  .contact-row { position: absolute; left: 40px; top: 37px; display: flex; align-items: center; font-size: 11.5px; color: #fff; white-space: nowrap; }
  .contact-row .sep { margin: 0 12px; font-size: 14px; }
  .contact-row svg { margin-right: 6px; }

  /* Envelope */
  .envelope { position: absolute; width: 719px; height: 311px; background: var(--paper); overflow: hidden; transform-origin: 0 0; }
  .envelope--main { left: 240px; top: 1005px; }
  .envelope--mini { left: 206px; top: 1689px; transform: scale(0.694); background: #f1f1f1; }
  .env-portrait { position: absolute; left: 0; top: 8px; width: 200px; height: 303px; background: linear-gradient(180deg, #f4f4f4 0%, #d9cfc6 22%, #1b1e26 45%, #0f1218 100%); }
  .env-faint { position: absolute; left: 546px; top: 40px; width: 173px; height: 193px; background: radial-gradient(ellipse at 55% 45%, #ddd9d4 0%, #ebe9e8 55%, rgba(255,255,255,0) 80%); }
  .env-art { position: absolute; left: 0; top: 0; }
  .env-slogan { position: absolute; left: 358px; width: 361px; top: 9px; text-align: center; font-family: "Libre Caslon Text", serif; font-size: 14.5px; color: var(--navy); letter-spacing: 0.3px; line-height: 1; }
  .env-web { position: absolute; left: 241px; top: 267px; display: flex; align-items: center; font-size: 12px; color: #fff; }
  .env-web svg { margin-right: 7px; }
  .env-brand { position: absolute; left: 458px; top: 258px; font-family: "Libre Caslon Text", serif; font-size: 26px; letter-spacing: 2px; color: var(--gold); line-height: 1; }
</style>
</head>
<body>
  <div class="stage-dark"></div>
  <div class="stage-light"></div>

  <!-- reusable letterhead (rendered twice) -->
  <section class="letterhead letterhead--main">
    <header class="lh-header">
      <svg width="719" height="87" viewBox="0 0 719 87">
        <defs>
          <linearGradient id="bandGold" x1="0" x2="1">
            <stop offset="0" stop-color="#c39d3c"/><stop offset="1" stop-color="#f8f1cc"/>
          </linearGradient>
          <linearGradient id="lineGold" x1="0" x2="1">
            <stop offset="0" stop-color="#f3c12f"/><stop offset="0.5" stop-color="#f7e7a8"/><stop offset="1" stop-color="#f8f1cc"/>
          </linearGradient>
        </defs>
        <rect x="0" y="81" width="719" height="6" fill="url(#lineGold)"/>
        <polygon points="380,47 719,47 719,81 346,81" fill="url(#bandGold)"/>
        <polygon points="342,47 352,47 318,81 308,81" fill="#c9a443"/>
        <polygon points="360,47 370,47 336,81 326,81" fill="#d8b756"/>
      </svg>
      <span class="brand-mark"></span>
      <span class="brand-name">BEACON LAW</span>
      <span class="tagline">Our Mission: To Fight and Win for you.</span>
    </header>

    <p class="date-line">Date:<span></span></p>

    <div class="lh-body">
      <p class="block" style="top:189px">Lorem Ipsum is simply dummy text of the printing and typesetting industry. Lorem Ipsum has been<br>the industry's standard dummy text ever since the 1500s, when an unknown printer took a galley<br>of type and scrambled it to make a type specimen book. It has survived not only five centuries, but<br>also the leap into electronic typesetting, remaining essentially unchanged. It was popularised in the</p>
      <h2 class="block section-key" style="top:269px">KEY TAKEAWAYS</h2>
      <p class="block" style="top:299px">Lorem Ipsum is simply dummy text of the printing and typesetting industry. Lorem Ipsum has been</p>
      <p class="check-item" style="top:328px"><svg width="14" height="13" viewBox="0 0 14 13"><rect x="1" y="2" width="10" height="10" fill="none" stroke="#0d1f4c" stroke-width="1.6"/><path d="M3.5 6.5l2.5 2.5 6.5-7.5" fill="none" stroke="#0d1f4c" stroke-width="2"/></svg>Lorem Ipsum is simply</p>
      <p class="check-item" style="top:349px"><svg width="14" height="13" viewBox="0 0 14 13"><rect x="1" y="2" width="10" height="10" fill="none" stroke="#0d1f4c" stroke-width="1.6"/><path d="M3.5 6.5l2.5 2.5 6.5-7.5" fill="none" stroke="#0d1f4c" stroke-width="2"/></svg>Lorem Ipsum is simply</p>
      <p class="check-item" style="top:370px"><svg width="14" height="13" viewBox="0 0 14 13"><rect x="1" y="2" width="10" height="10" fill="none" stroke="#0d1f4c" stroke-width="1.6"/><path d="M3.5 6.5l2.5 2.5 6.5-7.5" fill="none" stroke="#0d1f4c" stroke-width="2"/></svg>Lorem Ipsum is simply</p>
      <h3 class="block section-title" style="top:402px">Initial Access</h3>
      <p class="block" style="top:422px">Lorem Ipsum is simply dummy text of the printing and typesetting industry. Lorem Ipsum has<br>been the industry's standard dummy text ever since the 1500s, when an unknown printer took a</p>
      <p class="block" style="top:464px">Lorem Ipsum is simply dummy text of the printing and typesetting industry.<br>Lorem Ipsum has been the industry's standard dummy text ever since the 1500s,</p>
      <h3 class="block section-title" style="top:510px">Execution</h3>
      <p class="block" style="top:533px">Lorem Ipsum is simply dummy text of the printing and</p>
      <p class="check-item" style="top:560px"><svg width="14" height="13" viewBox="0 0 14 13"><rect x="1" y="2" width="10" height="10" fill="none" stroke="#0d1f4c" stroke-width="1.6"/><path d="M3.5 6.5l2.5 2.5 6.5-7.5" fill="none" stroke="#0d1f4c" stroke-width="2"/></svg>Lorem Ipsum is simply</p>
      <p class="check-item" style="top:581px"><svg width="14" height="13" viewBox="0 0 14 13"><rect x="1" y="2" width="10" height="10" fill="none" stroke="#0d1f4c" stroke-width="1.6"/><path d="M3.5 6.5l2.5 2.5 6.5-7.5" fill="none" stroke="#0d1f4c" stroke-width="2"/></svg>Lorem Ipsum is simply</p>
      <p class="check-item" style="top:602px"><svg width="14" height="13" viewBox="0 0 14 13"><rect x="1" y="2" width="10" height="10" fill="none" stroke="#0d1f4c" stroke-width="1.6"/><path d="M3.5 6.5l2.5 2.5 6.5-7.5" fill="none" stroke="#0d1f4c" stroke-width="2"/></svg>Lorem Ipsum is simply</p>
      <h3 class="block section-title" style="top:631px">Capabilities</h3>
      <p class="block" style="top:657px">Lorem Ipsum is simply dummy text of the printing and</p>
      <p class="check-item" style="top:689px"><svg width="14" height="13" viewBox="0 0 14 13"><rect x="1" y="2" width="10" height="10" fill="none" stroke="#0d1f4c" stroke-width="1.6"/><path d="M3.5 6.5l2.5 2.5 6.5-7.5" fill="none" stroke="#0d1f4c" stroke-width="2"/></svg>Lorem Ipsum is simply dummy text of the printing and typesetting industry. Lorem Ipsum</p>
      <p class="check-item" style="top:713px"><svg width="14" height="13" viewBox="0 0 14 13"><rect x="1" y="2" width="10" height="10" fill="none" stroke="#0d1f4c" stroke-width="1.6"/><path d="M3.5 6.5l2.5 2.5 6.5-7.5" fill="none" stroke="#0d1f4c" stroke-width="2"/></svg>Lorem Ipsum is simply dummy text of the</p>
      <p class="check-item" style="top:737px"><svg width="14" height="13" viewBox="0 0 14 13"><rect x="1" y="2" width="10" height="10" fill="none" stroke="#0d1f4c" stroke-width="1.6"/><path d="M3.5 6.5l2.5 2.5 6.5-7.5" fill="none" stroke="#0d1f4c" stroke-width="2"/></svg>Lorem Ipsum is simply dummy text of the printing and typesetting industry.<br>Lorem Ipsum has been the industry's standard dummy text ever since the<br>1500s, when an unknown printer took a galley of type and scrambled it to</p>
    </div>

    <footer class="lh-footer">
      <svg width="719" height="78" viewBox="0 0 719 78">
        <defs>
          <linearGradient id="footGold" x1="0" x2="1">
            <stop offset="0" stop-color="#f3c12f"/><stop offset="0.45" stop-color="#f6e8ad"/><stop offset="0.8" stop-color="#c9a443"/><stop offset="1" stop-color="#f5ecc4"/>
          </linearGradient>
        </defs>
        <polygon points="0,3 470,3 456,14 0,14" fill="url(#footGold)"/>
        <polygon points="480,0 719,0 719,78 0,78 0,17 458,17" fill="var(--navy-deep)"/>
      </svg>
      <div class="contact-row">
        <svg width="9" height="9" viewBox="0 0 10 10"><circle cx="5" cy="5" r="4.2" fill="none" stroke="#fff" stroke-width="1"/><path d="M1 5h8M5 1c-2 2.5-2 5.5 0 8M5 1c2 2.5 2 5.5 0 8" fill="none" stroke="#fff" stroke-width="0.8"/></svg>
        <span>www.beaconlawgroup.example</span><span class="sep">|</span>
        <svg width="10" height="8" viewBox="0 0 10 8"><rect x="0.5" y="0.5" width="9" height="7" fill="none" stroke="#fff"/><path d="M0.5 0.5l4.5 4 4.5-4" fill="none" stroke="#fff"/></svg>
        <span>help@beaconlawgroup.example</span><span class="sep">|</span>
        <svg width="10" height="10" viewBox="0 0 10 10"><path d="M2 1l2 2-1 1.5c.6 1.2 1.3 1.9 2.5 2.5L7 6l2 2-1.5 1.5C4 9 1 6 .5 2.5z" fill="none" stroke="#fff" stroke-width="0.9"/></svg>
        <span>(555) 014-2290</span>
      </div>
    </footer>
  </section>

  <section class="envelope envelope--main">
    <div class="env-portrait" role="img" aria-label="Portrait photo of the attorney in a dark suit"></div>
    <div class="env-faint" role="img" aria-label="Faint photo of a face with camouflage paint"></div>
    <svg class="env-art" width="719" height="311" viewBox="0 0 719 311">
      <defs>
        <linearGradient id="envGold" x1="0" x2="1">
          <stop offset="0" stop-color="#c6a03f"/><stop offset="1" stop-color="#f8f1cc"/>
        </linearGradient>
      </defs>
      <polygon points="330,0 719,0 719,32 358,32" fill="url(#envGold)"/>
      <polygon points="252,0 262,0 290,32 280,32" fill="var(--navy)"/>
      <polygon points="270,0 280,0 308,32 298,32" fill="var(--navy)"/>
      <polygon points="288,0 298,0 326,32 316,32" fill="var(--navy)"/>
      <polygon points="244,233 719,233 719,311 197,311" fill="var(--navy-deep)"/>
    </svg>
    <p class="env-slogan">A VETERAN OWNED LAW FIRM</p>
    <div class="env-web">
      <svg width="10" height="10" viewBox="0 0 10 10"><circle cx="5" cy="5" r="4.2" fill="none" stroke="#fff" stroke-width="1"/><path d="M1 5h8M5 1c-2 2.5-2 5.5 0 8M5 1c2 2.5 2 5.5 0 8" fill="none" stroke="#fff" stroke-width="0.8"/></svg>
      <span>www.beaconlawgroup.example</span>
    </div>
    <p class="env-brand">BEACON LAW</p>
  </section>

  <!-- second presentation -->
  <section class="letterhead letterhead--mini">
    <header class="lh-header">
      <svg width="719" height="87" viewBox="0 0 719 87">
        <defs>
          <linearGradient id="bandGold2" x1="0" x2="1">
            <stop offset="0" stop-color="#c39d3c"/><stop offset="1" stop-color="#f8f1cc"/>
          </linearGradient>
          <linearGradient id="lineGold2" x1="0" x2="1">
            <stop offset="0" stop-color="#f3c12f"/><stop offset="0.5" stop-color="#f7e7a8"/><stop offset="1" stop-color="#f8f1cc"/>
          </linearGradient>
        </defs>
        <rect x="0" y="81" width="719" height="6" fill="url(#lineGold2)"/>
        <polygon points="380,47 719,47 719,81 346,81" fill="url(#bandGold2)"/>
        <polygon points="342,47 352,47 318,81 308,81" fill="#c9a443"/>
        <polygon points="360,47 370,47 336,81 326,81" fill="#d8b756"/>
      </svg>
      <span class="brand-mark"></span>
      <span class="brand-name">BEACON LAW</span>
      <span class="tagline">Our Mission: To Fight and Win for you.</span>
    </header>

    <p class="date-line">Date:<span></span></p>

    <div class="lh-body">
      <p class="block" style="top:189px">Lorem Ipsum is simply dummy text of the printing and typesetting industry. Lorem Ipsum has been<br>the industry's standard dummy text ever since the 1500s, when an unknown printer took a galley<br>of type and scrambled it to make a type specimen book. It has survived not only five centuries, but<br>also the leap into electronic typesetting, remaining essentially unchanged. It was popularised in the</p>
      <h2 class="block section-key" style="top:269px">KEY TAKEAWAYS</h2>
      <p class="block" style="top:299px">Lorem Ipsum is simply dummy text of the printing and typesetting industry. Lorem Ipsum has been</p>
      <p class="block" style="top:422px">Lorem Ipsum is simply dummy text of the printing and typesetting industry. Lorem Ipsum has<br>been the industry's standard dummy text ever since the 1500s, when an unknown printer took a</p>
      <p class="block" style="top:464px">Lorem Ipsum is simply dummy text of the printing and typesetting industry.<br>Lorem Ipsum has been the industry's standard dummy text ever since the 1500s,</p>
      <p class="block" style="top:533px">Lorem Ipsum is simply dummy text of the printing and</p>
      <h3 class="block section-title" style="top:631px">Capabilities</h3>
      <p class="block" style="top:657px">Lorem Ipsum is simply dummy text of the printing and</p>
      <p class="check-item" style="top:689px"><svg width="14" height="13" viewBox="0 0 14 13"><rect x="1" y="2" width="10" height="10" fill="none" stroke="#0d1f4c" stroke-width="1.6"/><path d="M3.5 6.5l2.5 2.5 6.5-7.5" fill="none" stroke="#0d1f4c" stroke-width="2"/></svg>Lorem Ipsum is simply dummy text of the printing and typesetting industry. Lorem Ipsum</p>
      <p class="check-item" style="top:713px"><svg width="14" height="13" viewBox="0 0 14 13"><rect x="1" y="2" width="10" height="10" fill="none" stroke="#0d1f4c" stroke-width="1.6"/><path d="M3.5 6.5l2.5 2.5 6.5-7.5" fill="none" stroke="#0d1f4c" stroke-width="2"/></svg>Lorem Ipsum is simply dummy text of the</p>
      <p class="check-item" style="top:737px"><svg width="14" height="13" viewBox="0 0 14 13"><rect x="1" y="2" width="10" height="10" fill="none" stroke="#0d1f4c" stroke-width="1.6"/><path d="M3.5 6.5l2.5 2.5 6.5-7.5" fill="none" stroke="#0d1f4c" stroke-width="2"/></svg>Lorem Ipsum is simply dummy text of the printing and typesetting industry.<br>Lorem Ipsum has been the industry's standard dummy text ever since the<br>1500s, when an unknown printer took a galley of type and scrambled it to</p>
    </div>

    <footer class="lh-footer">
      <svg width="719" height="78" viewBox="0 0 719 78">
        <defs>
          <linearGradient id="footGold2" x1="0" x2="1">
            <stop offset="0" stop-color="#f3c12f"/><stop offset="0.45" stop-color="#f6e8ad"/><stop offset="0.8" stop-color="#c9a443"/><stop offset="1" stop-color="#f5ecc4"/>
          </linearGradient>
        </defs>
        <polygon points="0,3 470,3 456,14 0,14" fill="url(#footGold2)"/>
        <polygon points="480,0 719,0 719,78 0,78 0,17 458,17" fill="var(--navy-deep)"/>
      </svg>
      <div class="contact-row">
        <svg width="9" height="9" viewBox="0 0 10 10"><circle cx="5" cy="5" r="4.2" fill="none" stroke="#fff" stroke-width="1"/><path d="M1 5h8M5 1c-2 2.5-2 5.5 0 8M5 1c2 2.5 2 5.5 0 8" fill="none" stroke="#fff" stroke-width="0.8"/></svg>
        <span>www.beaconlawgroup.example</span><span class="sep">|</span>
        <svg width="10" height="8" viewBox="0 0 10 8"><rect x="0.5" y="0.5" width="9" height="7" fill="none" stroke="#fff"/><path d="M0.5 0.5l4.5 4 4.5-4" fill="none" stroke="#fff"/></svg>
        <span>help@beaconlawgroup.example</span><span class="sep">|</span>
        <svg width="10" height="10" viewBox="0 0 10 10"><path d="M2 1l2 2-1 1.5c.6 1.2 1.3 1.9 2.5 2.5L7 6l2 2-1.5 1.5C4 9 1 6 .5 2.5z" fill="none" stroke="#fff" stroke-width="0.9"/></svg>
        <span>(555) 014-2290</span>
      </div>
    </footer>
  </section>

  <section class="envelope envelope--mini">
    <div class="env-portrait" role="img" aria-label="Portrait photo of the attorney in a dark suit"></div>
    <div class="env-faint" role="img" aria-label="Faint photo of a face with camouflage paint"></div>
    <svg class="env-art" width="719" height="311" viewBox="0 0 719 311">
      <defs>
        <linearGradient id="envGold2" x1="0" x2="1">
          <stop offset="0" stop-color="#c6a03f"/><stop offset="1" stop-color="#f8f1cc"/>
        </linearGradient>
      </defs>
      <polygon points="330,0 719,0 719,32 358,32" fill="url(#envGold2)"/>
      <polygon points="252,0 262,0 290,32 280,32" fill="var(--navy)"/>
      <polygon points="270,0 280,0 308,32 298,32" fill="var(--navy)"/>
      <polygon points="288,0 298,0 326,32 316,32" fill="var(--navy)"/>
      <polygon points="244,233 719,233 719,311 197,311" fill="var(--navy-deep)"/>
    </svg>
    <p class="env-slogan">A VETERAN OWNED LAW FIRM</p>
    <div class="env-web">
      <svg width="10" height="10" viewBox="0 0 10 10"><circle cx="5" cy="5" r="4.2" fill="none" stroke="#fff" stroke-width="1"/><path d="M1 5h8M5 1c-2 2.5-2 5.5 0 8M5 1c2 2.5 2 5.5 0 8" fill="none" stroke="#fff" stroke-width="0.8"/></svg>
      <span>www.beaconlawgroup.example</span>
    </div>
    <p class="env-brand">BEACON LAW</p>
  </section>
</body>
</html>
```